Business Card Design

We are a cutting edge natural health care provider who specializes in neuro behavioral conditions. We use brain mapping, neurofeedback, functional neurology and functional medicine to help people achieve their health goals.
We need a business card design for a new office. Would like to position ourselves as an upscale/concierge level treatment center that provides hope and results to people with chronic conditions. We would like the card to feature a brain, possibly a die cut shape. Design needs to communicate our tag line of "providing excellent care for difficult cases."
On back side of card:
By retraining abnormal brainwave patterns and eliminating metabolic problems, our programs often improve symptoms of:
ADD/ADHD
Addiction
Anxiety
Autism
Depression
Fibromyalgia
Insomnia
Memory Loss
Sensory/Motor Dysfunction

Target Market(s)

30-60 year olds with chronic conditions (Anxiety, depression,) or parents of children with chronic conditions (ADHD, autism, learning disorders, etc)

Industry/Entity Type

Health

Contact Information for Business Card

The Halvorsen Clinic
Dr. Colin Halvorsen, DC
4260 Orchard Pkwy. Suite 207
Fairhaven, ST 10482
(555) 418-6623
Fax (555) 418-7044
www.TheHalvorsenClinic.example
www.DrColinHalvorsen.example

Requirements
Nice to have
• Picture of a brain that really pops on the page.

```html
<!DOCTYPE html>
<html lang="en">
<head>
<meta charset="utf-8">
<title>The Halvorsen Clinic – Business Card</title>
<link rel="stylesheet" href="https://fonts.googleapis.com/css2?family=Tinos&display=swap">
<style>
  :root {
    --brand-green: #3fa946;
    --band-grey: #e3e3e1;
    --card-white: #ffffff;
  }
  html, body {
    margin: 0;
    padding: 0;
    overflow: hidden;
    background: var(--card-white);
  }
  .card {
    position: relative;
    width: 1200px;
    height: 702px;
    background: var(--card-white);
    overflow: hidden;
    font-family: "Tinos", "Times New Roman", serif;
    color: var(--brand-green);
  }
  .doctor-name {
    position: absolute;
    left: 69px;
    top: 60px;
    margin: 0;
    font-size: 46px;
    font-weight: 400;
    line-height: 1;
    white-space: nowrap;
  }
  .band {
    position: absolute;
    background: var(--band-grey);
    box-sizing: border-box;
    white-space: nowrap;
  }
  .band--clinic {
    left: 367px;
    top: 187px;
    width: 370px;
    height: 76px;
    padding-left: 27px;
    font-size: 34px;
    line-height: 76px;
  }
  .band--tagline {
    left: 59px;
    top: 302px;
    width: 680px;
    height: 65px;
    padding-left: 10px;
    font-size: 31px;
    line-height: 65px;
  }
  .band--contact {
    left: 58px;
    top: 543px;
    width: 1092px;
    height: 101px;
    padding: 13px 0 0 9px;
    font-size: 31px;
    line-height: 37px;
    font-style: normal;
    letter-spacing: 0.3px;
  }
  .brand-mark {
    position: absolute;
    left: 719px;
    top: 72px;
    width: 412px;
    height: 412px;
  }
</style>
</head>
<body>
  <div class="card">
    <h1 class="doctor-name">Dr. Colin Halvorsen</h1>

    <div class="band band--clinic">The Halvorsen Clinic</div>
    <div class="band band--tagline">providing excellent care for difficult cases</div>

    <svg class="brand-mark" viewBox="0 0 412 412" role="img" aria-label="The Halvorsen Clinic">
      <circle cx="206" cy="206" r="206" fill="var(--brand-green)"/>
      <text x="206" y="217" text-anchor="middle" font-family="Tinos, 'Times New Roman', serif" font-size="32" fill="var(--card-white)">The Halvorsen Clinic</text>
    </svg>

    <address class="band band--contact">
      DC 4260 Orchard Pkwy. Suite 207 Fairhaven, ST 10482 (555) 418-6623<br>
      Fax (555) 418-7044 www.TheHalvorsenClinic.example
    </address>
  </div>
</body>
</html>
```